Business Card Design

I need a business card for my rental business. The business is named:
Hire a Vorlatrike Brenmoor
www.hireavorlatrikebrenmoor.example
(555) 014-2937
This will be a business card that I will leave at other businesses as advertisement so it needs to have the name, website, and phone number.
Please feel free to be creative. This is a new business so I have no designs.
Thank you very much for your time and I look forward to receiving your designs
Target Market(s)
Local rental customers
Industry/Entity Type
Business
Contact Information for Business Card
Please check out my website:
Other font styles liked:
- anything creative
Colors
Designer to choose colors to be used in the design.
Requirements
Must have
- Business name, phone, website. Rentals available hourly or daily. Book online

```html
<!DOCTYPE html>
<html lang="en">
<head>
<meta charset="utf-8">
<title>Hire a Vorlatrike Brenmoor – Business Card</title>
<link rel="stylesheet" href="https://fonts.googleapis.com/css2?family=Russo+One&family=Exo+2:ital,wght@1,800&family=Saira+Semi+Condensed:wght@300;400&display=swap">
<style>
  :root {
    --card-red: #c01f27;
    --ink-black: #070707;
    --paper-white: #ffffff;
    --muted-grey: #dcdcdc;
  }
  html, body {
    margin: 0;
    padding: 0;
    width: 1200px;
    height: 720px;
    overflow: hidden;
    background: var(--paper-white);
  }
  .business-card {
    display: block;
    width: 1200px;
    height: 720px;
  }
  .stripe, .red-field { fill: var(--card-red); }
  .title-band { fill: var(--paper-white); }
  .cta-banner, .cta-tail { fill: var(--ink-black); }
  .business-name {
    font-family: "Russo One", sans-serif;
    font-size: 112px;
    fill: var(--ink-black);
  }
  .cta-text {
    font-family: "Exo 2", sans-serif;
    font-style: italic;
    font-weight: 800;
    font-size: 52px;
    fill: var(--paper-white);
  }
  .website {
    font-family: "Saira Semi Condensed", sans-serif;
    font-weight: 400;
    font-size: 40px;
    fill: var(--paper-white);
  }
  .rental-note {
    font-family: "Saira Semi Condensed", sans-serif;
    font-weight: 300;
    font-size: 27px;
    fill: var(--muted-grey);
  }
  .contact-text {
    font-family: "Saira Semi Condensed", sans-serif;
    font-weight: 400;
    font-size: 36px;
    fill: var(--paper-white);
  }
  .icon-line {
    fill: none;
    stroke: var(--paper-white);
    stroke-width: 4;
    stroke-linejoin: round;
  }
  .icon-fill { fill: var(--paper-white); }
</style>
</head>
<body>
<svg class="business-card" viewBox="0 0 1500 900" width="1200" height="720" xmlns="http://www.w3.org/2000/svg">
  <!-- diagonal speed stripes -->
  <g class="speed-stripes">
    <polygon class="stripe" points="548,0 640,0 420,900 328,900"/>
    <polygon class="stripe" points="658,0 705,0 485,900 438,900"/>
    <polygon class="stripe" points="725,0 760,0 540,900 505,900"/>
    <polygon class="red-field" points="775,0 1500,0 1500,900 555,900"/>
  </g>

  <!-- name band -->
  <polygon class="title-band" points="0,130 1435,130 1405,255 0,255"/>
  <text class="business-name" x="122" y="236" textLength="1283" lengthAdjust="spacingAndGlyphs">HIRE A VORLATRIKE BRENMOOR</text>

  <!-- call to action -->
  <g class="cta">
    <polygon class="cta-banner" points="668,425 1385,425 1367,500 650,500"/>
    <polygon class="cta-tail" points="1390,425 1398,425 1380,500 1372,500"/>
    <polygon class="cta-tail" points="1403,425 1418,425 1400,500 1385,500"/>
    <text class="cta-text" x="682" y="482" textLength="660" lengthAdjust="spacingAndGlyphs">BOOK YOUR RIDE ONLINE</text>
  </g>

  <text class="website" x="652" y="545" textLength="540" lengthAdjust="spacingAndGlyphs">www.hireavorlatrikebrenmoor.example</text>
  <text class="rental-note" x="640" y="587" textLength="396" lengthAdjust="spacingAndGlyphs">Rentals available hourly and daily</text>

  <!-- contact row -->
  <g class="contact-email">
    <rect class="icon-line" x="612" y="795" width="46" height="32"/>
    <polyline class="icon-line" points="612,795 635,815 658,795"/>
    <text class="contact-text" x="672" y="822" textLength="320" lengthAdjust="spacingAndGlyphs">hirevorla@brenmoor.example</text>
  </g>
  <g class="contact-phone">
    <path class="icon-fill" d="M1176,790 l6,-2 l4,12 l-5,3 c-1,6 2,14 6,19 l5,-3 l8,10 l-5,4 c-8,2 -17,-10 -20,-20 c-3,-10 -3,-20 1,-23 z"/>
    <text class="contact-text" x="1200" y="822" textLength="218" lengthAdjust="spacingAndGlyphs">(555) 014-2937</text>
  </g>
</svg>
</body>
</html>
```